Webdesign für Hundeerziehungsberatung
Zielgruppe:
Hundehalter, die entweder einen Welpen angeschafft haben, ihren Hund ausbilden oder fördern wollen sowie Menschen mit einem 'Problemhund'.
Die Hundeerziehungsberatung bietet Hundehaltern die Erziehung im Einzelsetting und im Gruppensetting an.
Aufgabenstellung
die Farben sollen sich am Logo orientieren, gern noch eine Farbe dazu. Logo anbei, Bilder anbei. Flyer anbei
Sollten die Bilder ausreichen bitten wir um Auswahl bei pixel.morvani. Tool: Photoshop.
Der Kundin gefällt: https://www.pfotenlauf-brevik.de/

```html
<!DOCTYPE html>
<html lang="de">
<head>
<meta charset="utf-8">
<title>Hundeschule Spurweise in Chemnitz</title>
<link href="https://fonts.googleapis.com/css2?family=Montserrat:wght@300;400;600;700;800;900&family=Arimo:wght@400;700&display=swap" rel="stylesheet">
<style>
:root{
  --brown:#7d7366;
  --brown-dark:#6e6558;
  --heading:#7a7065;
  --text:#7f7873;
  --grey-light:#efefef;
  --shadow-blob:#c9c4bf;
  --button:#8c8580;
  --field:#9c948e;
  --footer-head:#a59d97;
  --white:#ffffff;
}
*{box-sizing:border-box;margin:0;padding:0}
html,body{width:1200px;height:4992px;overflow:hidden}
body{font-family:"Arimo",Arial,sans-serif;color:var(--text);background:var(--white);position:relative}
.abs{position:absolute}
.heading{font-family:"Montserrat",Arial,sans-serif;font-weight:900;color:var(--heading);text-transform:uppercase;letter-spacing:-0.5px}

/* header */
.site-header{position:absolute;top:0;left:0;width:1200px;height:107px;background:var(--white);border-bottom:1px solid #e5e2df}
.brand{position:absolute;left:93px;top:14px;display:flex;align-items:center;gap:12px}
.brand-mark{width:78px;height:78px;border-radius:50%;border:3px solid var(--heading)}
.brand-name{font-family:"Montserrat",sans-serif;font-weight:400;font-size:36px;color:var(--heading)}
.contact-top{position:absolute;top:38px;font-size:18px;color:var(--text);display:flex;align-items:center;gap:12px}
.menu-btn{position:absolute;left:1085px;top:40px;width:40px;height:26px}
.menu-btn span{display:block;height:4px;background:var(--button);margin-bottom:5px;border-radius:2px}

/* hero */
.hero{position:absolute;top:107px;left:0;width:1200px;height:701px}
.hero-photo{position:absolute;inset:0;background:linear-gradient(100deg,#b9975c 0%,#cfb07a 30%,#a8a39a 55%,#d5b87f 80%,#9a8458 100%)}
.hero-blob{position:absolute;left:58px;top:267px;width:420px;height:355px}
.hero-title{position:absolute;left:88px;top:405px;width:380px;text-align:center;font-family:"Montserrat",sans-serif;font-weight:900;font-size:40px;line-height:48px;color:var(--white);text-transform:uppercase}

/* intro */
.intro-title{left:93px;top:925px;font-size:31px;line-height:40px}
.body-copy{font-size:20px;line-height:33px;text-align:justify;color:var(--text)}
.intro-copy{left:93px;top:1062px;width:418px}
.paw{position:absolute;width:56px;height:56px}

/* offers */
.offers{position:absolute;top:1574px;left:0;width:1200px;height:868px;background:var(--brown)}
.offers-title{position:absolute;top:56px;width:1200px;text-align:center;font-family:"Montserrat",sans-serif;font-weight:900;font-size:32px;line-height:40px;color:var(--white);text-transform:uppercase}
.offers-sub{position:absolute;top:156px;width:1200px;text-align:center;font-size:20px;color:var(--white)}
.card{position:absolute;top:258px;width:310px;height:480px;background:var(--white);padding:6px;text-align:center}
.card-photo{height:226px;background:linear-gradient(160deg,#6c8a3f,#9bb860 55%,#3e3a35)}
.card-title{margin-top:25px;font-family:"Montserrat",sans-serif;font-weight:800;font-size:22px;color:var(--heading)}
.card-text{margin:14px auto 0;width:275px;font-size:15px;line-height:25.5px;color:var(--text)}
.card-btn{display:block;margin:18px auto 0;width:140px;height:38px;line-height:38px;background:var(--button);color:var(--white);font-family:"Montserrat",sans-serif;font-weight:700;font-size:12px}

/* team */
.team-title{top:2535px;width:1200px;text-align:center;font-size:34px}
.member-name{left:600px;top:2698px;font-family:"Montserrat",sans-serif;font-weight:400;font-size:28px;color:var(--heading)}
.member-copy{left:600px;top:2762px;width:524px}
.claim{top:3160px;width:1200px;text-align:center;font-family:"Montserrat",sans-serif;font-weight:300;font-size:44px;color:#8a8580;letter-spacing:1px}

/* testimonials */
.testimonials{position:absolute;top:3333px;left:0;width:1200px;height:853px;background:var(--grey-light)}
.testi-title{position:absolute;top:50px;width:1200px;text-align:center;font-size:34px;line-height:47px}
.quote-mark{position:absolute;left:140px;top:440px;width:80px;height:64px}
.testi-text{position:absolute;left:130px;top:527px;width:940px;text-align:center;font-size:15.5px;line-height:35px;color:var(--text)}
.testi-author{position:absolute;top:670px;width:1200px;text-align:center;font-family:"Montserrat",sans-serif;font-weight:700;font-size:15px;color:var(--heading)}
.dots{position:absolute;top:734px;left:546px;display:flex;gap:14px}

/* footer (all positions relative to footer) */
.site-footer{position:absolute;top:4186px;left:0;width:1200px;height:806px;background:var(--brown-dark);color:var(--white)}
.foot-head{position:absolute;font-family:"Montserrat",sans-serif;font-weight:900;font-size:34px;line-height:45px;color:var(--footer-head);text-transform:uppercase}
.foot-text{position:absolute;font-size:17px;line-height:32px}
.news-field{position:absolute;left:93px;top:270px;width:426px;height:57px;background:var(--field);display:flex}
.news-field span{flex:1;padding-left:14px;line-height:57px;font-size:13px}
.news-field b{width:70px;background:#807873;display:flex;align-items:center;justify-content:center}
.contact-row{position:absolute;left:93px;height:30px;display:flex;align-items:center;gap:20px;font-size:17px;line-height:30px}
.contact-row svg{width:28px;height:28px;flex:none}
.social-list{position:absolute;left:93px;top:686px;display:flex;gap:22px}
.social{display:block;width:40px;height:40px;border-radius:50%;background:#8f8781}
.form-text{position:absolute;left:600px;top:146px;font-size:21px;line-height:30px;width:540px}
.field{position:absolute;background:var(--field)}
.check{position:absolute;left:600px;top:622px;width:26px;height:26px;background:var(--field)}
.check-label{position:absolute;left:645px;top:626px;font-size:14px}
.send-btn{position:absolute;left:600px;top:678px;width:154px;height:58px;background:var(--field);line-height:58px;text-align:center;font-family:"Montserrat",sans-serif;font-weight:600;font-size:15px}
</style>
</head>
<body>

<svg width="0" height="0" style="position:absolute">
  <defs>
    <path id="blob" d="M58 3 C74 0 84 18 95 44 C104 68 92 88 66 88 L26 86 C6 85 -2 70 6 55 L36 13 C43 5 50 4 58 3Z"/>
    <g id="paw-shape">
      <ellipse cx="50" cy="66" rx="22" ry="18"/>
      <ellipse cx="22" cy="42" rx="9" ry="12"/>
      <ellipse cx="40" cy="26" rx="9" ry="12"/>
      <ellipse cx="62" cy="26" rx="9" ry="12"/>
      <ellipse cx="79" cy="42" rx="9" ry="12"/>
    </g>
    <linearGradient id="g-dogs" x1="0" y1="0" x2="0" y2="1"><stop offset="0" stop-color="#8fb0d8"/><stop offset=".45" stop-color="#a89c86"/><stop offset="1" stop-color="#5f8a3a"/></linearGradient>
    <linearGradient id="g-team" x1="0" y1="0" x2="1" y2="1"><stop offset="0" stop-color="#c99a52"/><stop offset=".5" stop-color="#b6b3ad"/><stop offset="1" stop-color="#8a7e62"/></linearGradient>
    <linearGradient id="g-client" x1="0" y1="0" x2="1" y2="0"><stop offset="0" stop-color="#6b6560"/><stop offset=".5" stop-color="#d9d3c9"/><stop offset="1" stop-color="#c9a56a"/></linearGradient>
  </defs>
</svg>

<header class="site-header">
  <div class="brand"><div class="brand-mark"></div><span class="brand-name">Pfotenweg</span></div>
  <div class="contact-top" style="left:607px">
    <svg width="24" height="24" viewBox="0 0 24 24" fill="none" stroke="#8c8580" stroke-width="1.6"><path d="M5 3l4 1 1 5-2 2c1 3 3 5 6 6l2-2 5 1 1 4c-1 2-3 2-5 2C9 22 2 15 2 7c0-2 1-4 3-4z"/></svg>
    0170 – 318 442 105</div>
  <div class="contact-top" style="left:843px">
    <svg width="24" height="24" viewBox="0 0 24 24" fill="none" stroke="#8c8580" stroke-width="1.8"><circle cx="12" cy="12" r="4"/><path d="M16 12v2a3 3 0 006 0v-2a10 10 0 10-4 8"/></svg>
    info@pfotenweg.de</div>
  <div class="menu-btn"><span></span><span></span><span></span></div>
</header>

<section class="hero">
  <div class="hero-photo" role="img" aria-label="Foto: Trainerin kniet im herbstlichen Gras vor einem schwarz-weißen Hund"></div>
  <svg class="hero-blob" viewBox="0 0 100 90" preserveAspectRatio="none">
    <use href="#blob" fill="#a29b94" transform="translate(-4 6)"/>
    <use href="#blob" fill="#7d7366"/>
  </svg>
  <h1 class="hero-title">Hundeschule Spurweise in Chemnitz</h1>
</section>

<section>
  <h2 class="abs heading intro-title">Hund Spurweise<br>vielfältige Angebote<br>warten auf dich</h2>
  <p class="abs body-copy intro-copy">Lorem ipsum dolor sit amet, consectetuer adipiscing elit. Aenean commodo ligula eget dolor. Aenean massa. Cum sociis natoque penatibus et magnis dis parturient montes, nascetur ridiculus mus. Donec quam felis, ultricies nec, pellentesque eu, pretium quis, sem. Nulla consequat massa quis enim. Donec pede justo, fringilla vel, aliquet nec, vulputate eget, arcu. In enim justo, rhoncus ut, imperdiet a, venenatis vitae, justo. Nullam dictum felis eu pede mollis pretium. Integer tincidunt.</p>
  <svg class="abs" style="left:600px;top:985px" width="510" height="420" viewBox="0 0 100 90" preserveAspectRatio="none" role="img" aria-label="Foto: zwei Hunde toben auf einer Wiese">
    <use href="#blob" fill="var(--shadow-blob)" transform="translate(-5 5)"/>
    <use href="#blob" fill="url(#g-dogs)"/>
  </svg>
  <svg class="paw" style="left:1042px;top:988px" viewBox="0 0 100 100" fill="var(--heading)"><use href="#paw-shape" transform="rotate(15 50 50)"/></svg>
  <svg class="paw" style="left:1054px;top:1068px" viewBox="0 0 100 100" fill="var(--heading)"><use href="#paw-shape" transform="rotate(25 50 50)"/></svg>
</section>

<section class="offers">
  <h2 class="offers-title">Hund Spurweise<br>vielfältige Angebote warten</h2>
  <p class="offers-sub">Lorem ipsum dolor sit amet, consectetuer adipiscing elit.</p>
  <article class="card" style="left:93px">
    <div class="card-photo" role="img" aria-label="Foto: Hund schnuppert im hohen Gras"></div>
    <h3 class="card-title">EINZELCOACHING</h3>
    <p class="card-text">Lorem ipsum dolor sit amet, consectetuer adipiscing elit. Aenean commodo ligula eget dolor. Aenean massa. Integer tincidunt.</p>
    <span class="card-btn">Mehr Wissen</span>
  </article>
  <article class="card" style="left:453px">
    <div class="card-photo" role="img" aria-label="Foto: mehrere Hunde spielen auf dem Rasen"></div>
    <h3 class="card-title">EINZELCOACHING</h3>
    <p class="card-text">Lorem ipsum dolor sit amet, consectetuer adipiscing elit. Aenean commodo ligula eget dolor. Aenean massa. Integer tincidunt.</p>
    <span class="card-btn">Mehr Wissen</span>
  </article>
  <article class="card" style="left:814px">
    <div class="card-photo" role="img" aria-label="Foto: Hund schnuppert im hohen Gras"></div>
    <h3 class="card-title">EINZELCOACHING</h3>
    <p class="card-text">Lorem ipsum dolor sit amet, consectetuer adipiscing elit. Aenean commodo ligula eget dolor. Aenean massa. Integer tincidunt.</p>
    <span class="card-btn">Mehr Wissen</span>
  </article>
</section>

<section>
  <h2 class="abs heading team-title">Das Team</h2>
  <svg class="paw" style="left:58px;top:2645px" viewBox="0 0 100 100" fill="var(--heading)"><use href="#paw-shape" transform="rotate(-10 50 50)"/></svg>
  <svg class="paw" style="left:68px;top:2728px" viewBox="0 0 100 100" fill="var(--heading)"><use href="#paw-shape" transform="rotate(10 50 50)"/></svg>
  <svg class="abs" style="left:68px;top:2670px" width="495" height="422" viewBox="0 0 100 90" preserveAspectRatio="none" role="img" aria-label="Foto: Trainerin mit ihrem Hund im Herbst">
    <use href="#blob" fill="var(--shadow-blob)" transform="translate(-3 5)"/>
    <use href="#blob" fill="url(#g-team)"/>
  </svg>
  <h3 class="abs member-name">LENA MARBACH</h3>
  <p class="abs body-copy member-copy">Lorem ipsum dolor sit amet, consectetuer adipiscing elit. Aenean commodo ligula eget dolor. Aenean massa. Cum sociis natoque penatibus et magnis dis parturient montes, nascetur ridiculus mus. Donec quam felis, ultricies nec, pellentesque eu, pretium quis, sem. Nulla consequat massa quis enim. Donec pede justo, fringilla vel, aliquet nec, vulputate eget, arcu. In enim justo, rhoncus ut, imperdiet a, venenatis vitae, justo. Nullam dictum felis eu pede mollis pretium. Integer tincidunt.</p>
  <p class="abs claim">AUTHENTISCH - RESPEKTVOLL - INDIVIDUELL</p>
</section>

<section class="testimonials">
  <h2 class="heading testi-title">Den Weg als Ziel sehe<br>Kundenstimmen</h2>
  <svg class="abs" style="left:401px;top:188px" width="342" height="290" viewBox="0 0 100 90" preserveAspectRatio="none" role="img" aria-label="Foto: Mann gibt seinem Golden Retriever High Five">
    <use href="#blob" fill="#8a847e" transform="translate(-3 5)"/>
    <use href="#blob" fill="url(#g-client)"/>
  </svg>
  <svg class="quote-mark" viewBox="0 0 80 64" fill="#8c8580"><path d="M0 30C0 12 10 2 26 0v10C16 13 13 20 13 26h19v38H0zM46 30C46 12 56 2 72 0v10c-10 3-13 10-13 16h19v38H46z"/></svg>
  <p class="testi-text">Danke, lieber Tobias, für deine Ruhe, deine Geduld und Ausgeglichenheit sowie die vielen guten Tipps aus einer für mich anfangs ungewohnten Perspektive. Heute bin ich froh, dass ich mich darauf eingelassen habe, neue Wege in der Hundeerziehung zu gehen. Aus meiner hyperaktiven Goldendoodle-Hündin Inka ist eine ausgeglichene, zufrieden wirkende Begleiterin geworden. Auch unsere Verwandten, Freunde und Nachbarn bestätigen den charakterlichen Wandel seit Juni 2016 immer wieder. Danke!</p>
  <p class="testi-author">Greta Sollwerk</p>
  <div class="dots">
    <svg width="26" height="26" viewBox="0 0 100 100" fill="#6e6558"><use href="#paw-shape"/></svg>
    <svg width="26" height="26" viewBox="0 0 100 100" fill="#bdb8b3"><use href="#paw-shape"/></svg>
    <svg width="26" height="26" viewBox="0 0 100 100" fill="#bdb8b3"><use href="#paw-shape"/></svg>
  </div>
</section>

<footer class="site-footer">
  <h2 class="foot-head" style="left:93px;top:96px">Unser<br>Newsletter</h2>
  <p class="foot-text" style="left:93px;top:196px;width:440px">Lorem ipsum dolor sit amet, consectetuer adipiscing elit. Aenean commodo ligula eget dolor.</p>
  <div class="news-field"><span>Email</span><b><svg width="18" height="30" viewBox="0 0 18 30" fill="none" stroke="#fff" stroke-width="2.5"><path d="M3 3l12 12L3 27"/></svg></b></div>

  <h2 class="foot-head" style="left:93px;top:412px">Kontakt</h2>
  <p class="foot-text" style="left:93px;top:458px">Hundeschule Spurweise</p>
  <div class="contact-row" style="top:502px">
    <svg viewBox="0 0 24 24" fill="none" stroke="#fff" stroke-width="1.5"><path d="M12 22s7-7 7-12a7 7 0 00-14 0c0 5 7 12 7 12z"/><circle cx="12" cy="10" r="2.5"/></svg>
    Aenean commodo ligula eget dolor.</div>
  <div class="contact-row" style="top:545px">
    <svg viewBox="0 0 24 24" fill="none" stroke="#fff" stroke-width="1.5"><path d="M5 3l4 1 1 5-2 2c1 3 3 5 6 6l2-2 5 1 1 4c-1 2-3 2-5 2C9 22 2 15 2 7c0-2 1-4 3-4z"/></svg>
    0170 – 318 442 105</div>
  <div class="contact-row" style="top:587px">
    <svg viewBox="0 0 24 24" fill="none" stroke="#fff" stroke-width="1.8"><circle cx="12" cy="12" r="4"/><path d="M16 12v2a3 3 0 006 0v-2a10 10 0 10-4 8"/></svg>
    info@pfotenweg.de</div>
  <div class="social-list">
    <span class="social" aria-label="Soziales Netzwerk"></span>
    <span class="social" aria-label="Soziales Netzwerk"></span>
    <span class="social" aria-label="Soziales Netzwerk"></span>
  </div>

  <h2 class="foot-head" style="left:600px;top:96px">Du hast eine Frage?</h2>
  <p class="form-text">DANN SCHREIBE UNS!<br>Du möchtest mehr zu unserem Angebot erfahren,<br>hast eine individuelle Frage<br>oder möchtest Dein Erstgespräch vereinbaren?</p>
  <p class="form-text" style="top:280px">Wir freuen uns von Dir zu hören!</p>
  <div class="field" style="left:600px;top:326px;width:252px;height:58px"></div>
  <div class="field" style="left:871px;top:326px;width:253px;height:58px"></div>
  <div class="field" style="left:600px;top:404px;width:524px;height:58px"></div>
  <div class="field" style="left:600px;top:483px;width:524px;height:108px"></div>
  <div class="check"></div>
  <p class="check-label">Die Datenschutzerklärung wurden gelesen und hiermit bestätigt</p>
  <div class="send-btn">SENDEN</div>
</footer>

</body>
</html>
```